Theatre Company needs a Poster design for a world premiere of "Ember Hollow" Play.

We are premiering a play that celebrates community in rural and regional Australia . We need a poster for A3 and A5 size and an image that can be used in our email correspondence/webpage.

Attached is some ideas the producing theatre committee has come up with, a river runs through the town itself.

Town

```html
<!DOCTYPE html>
<html lang="en">
<head>
<meta charset="utf-8">
<title>Ember Hollow — Poster</title>
<link rel="stylesheet" href="https://fonts.googleapis.com/css2?family=Cormorant+Garamond:ital,wght@0,500;0,600;1,500&family=Playfair+Display:wght@400&display=swap">
<style>
  :root {
    --ink-white: #f7f1ee;
    --tree-dark: #1f1f1f;
    --tree-mid: #4a4a4a;
    --lawn-light: #cfcfcf;
    --water-dark: #161616;
    --plank-mid: #5c5c5c;
    --plank-light: #8a8a8a;
    --ember-red: rgba(176, 40, 32, 0.74);
    --ember-band: rgba(140, 34, 28, 0.88);
  }
  * { margin: 0; padding: 0; box-sizing: border-box; }
  html, body { width: 849px; height: 1200px; overflow: hidden; background: #ffffff; }
  .poster {
    position: relative;
    width: 849px;
    height: 1200px;
    overflow: hidden;
    font-family: "Cormorant Garamond", serif;
    color: var(--ink-white);
  }
  .poster__photo {
    position: absolute;
    inset: 0;
    background:
      /* bridge deck narrowing into the distance */
      radial-gradient(ellipse 34% 62% at 44% 100%, var(--plank-light) 0%, var(--plank-mid) 55%, transparent 100%),
      /* dark water to the left and right of the bridge */
      radial-gradient(ellipse 30% 45% at 0% 85%, var(--water-dark) 0%, transparent 100%),
      radial-gradient(ellipse 26% 40% at 100% 90%, var(--water-dark) 0%, transparent 100%),
      /* bright lawn on the far bank */
      radial-gradient(ellipse 40% 14% at 88% 40%, var(--lawn-light) 0%, #a8a8a8 50%, transparent 100%),
      radial-gradient(ellipse 30% 10% at 6% 42%, #9c9c9c 0%, transparent 100%),
      /* dense trees along the top */
      radial-gradient(ellipse 35% 22% at 80% 12%, #3a3a3a 0%, transparent 100%),
      radial-gradient(ellipse 30% 24% at 10% 8%, #8c8c8c 0%, transparent 100%),
      linear-gradient(180deg, var(--tree-mid) 0%, var(--tree-dark) 25%, #777 40%, #505050 55%, #2e2e2e 80%, #1a1a1a 100%);
  }
  .poster__disc {
    position: absolute;
    left: 48px;
    top: 96px;
    width: 617px;
    height: 617px;
    border-radius: 50%;
    background: var(--ember-red);
  }
  .poster__heading {
    position: absolute;
    left: 72px;
    top: 272px;
    width: 564px;
    text-align: center;
  }
  .poster__presenter {
    font-size: 19px;
    font-weight: 600;
    letter-spacing: 1px;
    text-transform: uppercase;
    white-space: nowrap;
  }
  .poster__rule {
    height: 1px;
    background: rgba(247, 241, 238, 0.7);
    margin: 12px 0;
  }
  .poster__title {
    font-family: "Playfair Display", serif;
    font-weight: 400;
    font-size: 70px;
    line-height: 1;
    letter-spacing: 1px;
    text-transform: uppercase;
    white-space: nowrap;
  }
  .poster__credit {
    font-size: 17px;
    font-weight: 600;
    letter-spacing: 1px;
    text-transform: uppercase;
    white-space: nowrap;
  }
  .poster__tagline {
    position: absolute;
    left: 235px;
    top: 1098px;
    width: 600px;
    height: 68px;
    background: var(--ember-band);
    padding: 6px;
  }
  .poster__tagline-frame {
    width: 100%;
    height: 100%;
    border: 1px solid rgba(247, 241, 238, 0.7);
    display: flex;
    align-items: center;
    justify-content: center;
    font-style: italic;
    font-weight: 500;
    font-size: 28px;
    white-space: nowrap;
  }
</style>
</head>
<body>
  <main class="poster">
    <div class="poster__photo" role="img" aria-label="Black and white photograph of a long wooden footbridge with railings running over dark river water toward a bright lawn and dense trees"></div>
    <div class="poster__disc"></div>
    <header class="poster__heading">
      <p class="poster__presenter">Millbrook Theatre Company presents to you</p>
      <div class="poster__rule"></div>
      <h1 class="poster__title">Ember Hollow</h1>
      <div class="poster__rule"></div>
      <p class="poster__credit">Written by Dana Whitlow</p>
    </header>
    <aside class="poster__tagline">
      <p class="poster__tagline-frame">“a river runs through the town itself”</p>
    </aside>
  </main>
</body>
</html>
```